Business cards Dorn Kelterhof GmbH & Co.KG

We need a uniform business card design template for our employees.
A template should be created to have the same design for all business cards.

Contact Information for Business Card

Firma und Firmierung, Name, Funktion in Unternehmen, Anschrift, Tel. Handynummer, Emailadresse, Internetseite

Colors

Designer to choose colors to be used in the design.

Requirements
Must have
• Our company logo must be on it

```html
<!DOCTYPE html>
<html lang="de">
<head>
<meta charset="utf-8">
<title>Dorn Kelterhof – Visitenkarte</title>
<link rel="stylesheet" href="https://fonts.googleapis.com/css2?family=Source+Sans+3:wght@400;600&display=swap">
<style>
  :root {
    --stage: #d9d9db;
    --card-dark: #2d2b2b;
    --card-light: #ffffff;
    --lavender: #c39bd3;
    --rose: #e8677a;
    --ink: #1f1f1f;
  }
  html, body {
    margin: 0;
    width: 1200px;
    height: 800px;
    overflow: hidden;
    background: var(--stage);
    font-family: "Source Sans 3", "Myriad Pro", sans-serif;
  }
  .stage {
    position: relative;
    width: 1200px;
    height: 800px;
  }
  .card {
    position: absolute;
    top: 240px;
    width: 525px;
    height: 300px;
    box-sizing: border-box;
    box-shadow: 0 6px 18px rgba(0,0,0,0.18);
  }
  .card--front {
    left: 50px;
    background: var(--card-dark);
    display: flex;
    align-items: center;
    justify-content: center;
  }
  .card--back {
    left: 625px;
    background: var(--card-light);
    padding: 34px 38px;
  }
  .brand-name {
    margin: 0;
    color: var(--lavender);
    font-weight: 600;
    letter-spacing: 0.5px;
  }
  .card--front .brand-name { font-size: 46px; }
  .card--back .brand-name { font-size: 32px; margin-bottom: 26px; }
  .person-name {
    margin: 0;
    color: var(--lavender);
    font-weight: 600;
    font-size: 20px;
    line-height: 1.1;
  }
  .person-role {
    margin: 0 0 18px;
    color: var(--ink);
    font-size: 15px;
  }
  .contact {
    margin: 0;
    padding: 0;
    list-style: none;
    color: var(--ink);
    font-size: 15px;
    line-height: 1.35;
  }
  .contact-item {
    display: flex;
    align-items: center;
    gap: 7px;
  }
  .contact-item--plain { padding-left: 0; }
  .contact-icon {
    width: 12px;
    height: 12px;
    flex: none;
  }
</style>
</head>
<body>
<main class="stage">
  <section class="card card--front">
    <h1 class="brand-name">Dorn Kelterhof</h1>
  </section>

  <section class="card card--back">
    <h2 class="brand-name">Dorn Kelterhof</h2>
    <p class="person-name">Hanna Lindqvist</p>
    <p class="person-role">Founder</p>
    <ul class="contact">
      <li class="contact-item contact-item--plain">Weinbergstraße 12</li>
      <li class="contact-item contact-item--plain">54470 Bernkastel-Kues</li>
      <li class="contact-item">
        <svg class="contact-icon" viewBox="0 0 24 24" aria-hidden="true"><path fill="#e8677a" d="M6.6 10.8a15.1 15.1 0 0 0 6.6 6.6l2.2-2.2c.3-.3.7-.4 1-.2 1.1.4 2.3.6 3.6.6.6 0 1 .4 1 1V20c0 .6-.4 1-1 1A17 17 0 0 1 3 4c0-.6.4-1 1-1h3.5c.6 0 1 .4 1 1 0 1.3.2 2.5.6 3.6.1.3 0 .7-.2 1z"/></svg>
        +49 6531 48210
      </li>
      <li class="contact-item">
        <svg class="contact-icon" viewBox="0 0 24 24" aria-hidden="true"><rect x="2" y="5" width="20" height="14" fill="none" stroke="#e8677a" stroke-width="2"/><path d="M2 5l10 8 10-8" fill="none" stroke="#e8677a" stroke-width="2"/></svg>
        hanna@dornkelterhof.de
      </li>
      <li class="contact-item">
        <svg class="contact-icon" viewBox="0 0 24 24" aria-hidden="true"><g fill="none" stroke="#e8677a" stroke-width="2"><circle cx="12" cy="12" r="10"/><ellipse cx="12" cy="12" rx="4" ry="10"/><path d="M2 12h20"/></g></svg>
        www.dornkelterhof.de
      </li>
    </ul>
  </section>
</main>
</body>
</html>
```